GUARANTEED 4 sample word cards for inclusive primary education (the swan, the icebear, the cat, sad)

in short: it's about drawing a swan, at icebear, a cat, a sad person (male / female) and arranging them on word cards with some additional information As there which only one design submitted, Which was missing the point I Decided to translate everything myself and upload it again. Requirements Within an open educational ressources (OER) project, materials for the interest-based spelling workout are to be created. In the preparation of this project four example sample word cards are to be developed. Later They Should be compiled dynamically from a database. Since the needs of the teachers are very different, it would be advantageous to integrate the different design elements as layers in Photoshop so did one can show how diverse the cards can look later by hiding / showing the layers. The materials shoulderstand be distributed under cc-0 license. It is about 4 sample cards (the swan, the icebear, the cat, sad), Which shoulderstand demonstrate how search cards can look. German: As part of an OER project are materials to interest-based spelling learning occur. In the preparation of the project (to be created also a permanent position for a / n Designer / -in under which) are four examplarische Sample word cards are developed. Later this should be assembled dynamically from a database. Since the needs of teachers / -Innen are very different, it would be desirable to integrate the various design elements as layers in Photoshop, so you can show how diverse can look the cards later. The materials are to be distributed under cc-0 license. It is about 4 example cards that demonstrate how can such cards look. The most expensive part is undoubtedly the drawings (polar bear, swan, cat and sad child / sad person). Common elements - speech symbol Lindqvist (see http: //media.brenzo-haus. de / media / catalog / product / cache / 4 / image / 3ab41cde77280f19e4c2da6b58190a42 / 0/7 / 07216_1.jpg) - underline articles colored or colored or point mark (male - red, male - blue, neuter - green) - writing of definition and article (once https://typevault.example/en/font/grundschrift and once a school Ausgangsschrift eg https://www.vorlind.example/pulse/Tavrel/de_DE.CMS.displayCMS.209797./die-schulausgangsschrift -sas-free-download-vorlind) - Ruling based on http://www.t-wellbrig.example/wp-content/uploads/2010/01/Heft-006-innen.png (and even without house) - picture on the right side - pictures with people, each as a girl / boy, different skin colors (or all as layers in Photoshop, where I can hide it myself) - syllable sheets (instead of the | http://tryclassmill.example/wp- content / uploads / 2015_2_Silbenboegen_Kombo.png) - colored syllables (blue and red) - stem color (red), ending black - cases if necessary on the back of the card - Format Din A7, rounded corners images should as svg / or levels exist (different skin color / hair color / gender) drawings should stylized and not be too childish and love of detail, so that they are attractive to adults (and as can be used in work with fugitives). You should also black / white and be usable with red / green blindness. The exact requirements are in the description file. For any questions please contact via the platform or paulr.hessling@hs-tarnow.example Ps: If a logo for (spelling) learning, including drops, it is also nich bad;) If you interested in a long-term employment in a project have the university, we appreciate if you mention this.
Target Market(s)
pupils in primary school, so but older students and adults (for example refugees who started to learn the language) students / -Innen primary school (until fourth grade) as well as older adolescents / adults, therefore, not to child pictures
Industry/Entity Type
Education
Font styles to use
Other font styles liked:
- see additional file

Requirements
Must have
- psd files with levels, to show and hide different elements self drawn images, Which Could be released under a CC-0 license. see additional file for more info and sample German: .psd files with labeled layers, in which the individual elements can be hidden. Self-drawn graphics which can then be released under cc-0 Stock

```html
<!DOCTYPE html>
<html lang="de">
<head>
<meta charset="utf-8">
<title>Wortkarte – der Schwan</title>
<link href="https://fonts.googleapis.com/css2?family=Andika:wght@400;700&family=Open+Sans:wght@700;800&display=swap" rel="stylesheet">
<style>
  :root {
    --page-bg: #d4d4d4;
    --front-bg-light: #ffffff;
    --front-bg-tint: #cfe9f8;
    --back-bg-light: #f6f6fa;
    --back-bg-tint: #d4d5ee;
    --ink: #1a1a1a;
    --article-blue: #1aa3ea;
    --plural-grey: #8a8a8a;
    --rule: #c9c9c9;
    --house: #9a9a9a;
    --tag-bg: #0e6aa6;
    --tag-text: #ffffff;
    --case-blue: #2a8fe6;
    --table-line: #5a5a5a;
    --swan-blue: #15589a;
  }
  * { box-sizing: border-box; margin: 0; padding: 0; }
  html, body { width: 1200px; height: 1000px; overflow: hidden; }
  body { background: var(--page-bg); position: relative; font-family: "Andika", sans-serif; color: var(--ink); }

  .card {
    position: absolute;
    border-radius: 14px;
    overflow: hidden;
    box-shadow: 0 3px 10px rgba(0,0,0,0.25);
  }

  /* Front */
  .card--front {
    left: 30px; top: 22px; width: 676px; height: 476px;
    background:
      radial-gradient(circle at 90% 15%, var(--front-bg-tint) 0, transparent 45%),
      radial-gradient(circle at 10% 85%, var(--front-bg-tint) 0, transparent 50%),
      linear-gradient(160deg, #eaf6fd 0%, var(--front-bg-light) 45%, #e3f2fb 100%);
  }
  .writing-band {
    position: absolute; left: 0; top: 19px; width: 402px; height: 207px;
    background: var(--front-bg-light);
  }
  .ruling { position: absolute; left: 16px; width: 386px; }
  .ruling svg { display: block; }
  .ruling--singular { top: 28px; }
  .ruling--plural { top: 126px; }
  .word {
    position: absolute; left: 76px;
    font-size: 52px; line-height: 1; white-space: nowrap;
  }
  .word--singular { top: 40px; }
  .word--plural { top: 137px; }
  .word .article { color: var(--article-blue); }
  .word--plural .article { color: var(--plural-grey); }

  .word-class {
    position: absolute; left: 504px; top: 22px;
    display: flex; align-items: flex-end; gap: 6px;
    font-size: 29px; line-height: 1;
  }
  .word-class svg { display: block; }

  .picture {
    position: absolute; left: 445px; top: 90px; width: 185px; height: 172px;
    border-radius: 50% 40% 45% 50%;
    background: radial-gradient(circle at 55% 55%, var(--swan-blue) 0, #2b6fb0 70%, transparent 72%);
  }

  .example-sentence {
    position: absolute; left: 16px; top: 294px;
    font-size: 31px; line-height: 1.2; white-space: nowrap;
  }

  .tags {
    position: absolute; left: 19px; top: 407px; width: 408px; height: 50px;
    background: var(--tag-bg); border-radius: 3px;
    display: flex; align-items: center; justify-content: center; gap: 14px;
    font-family: "Open Sans", sans-serif; font-weight: 800; font-size: 24px;
    color: var(--tag-text); white-space: nowrap;
  }

  /* Back */
  .card--back {
    left: 430px; top: 509px; width: 674px; height: 477px;
    background:
      radial-gradient(circle at 95% 10%, var(--back-bg-tint) 0, transparent 40%),
      radial-gradient(circle at 5% 90%, var(--back-bg-tint) 0, transparent 45%),
      linear-gradient(170deg, #e4e4f3 0%, var(--back-bg-light) 50%, #e2e2f2 100%);
  }
  .case-band {
    position: absolute; left: 0; top: 93px; width: 100%; height: 302px;
    background: rgba(248,248,250,0.75);
  }
  .case-table { position: absolute; left: 19px; top: 114px; width: 635px; }
  .case-table .top-line {
    position: absolute; left: 247px; right: 0; top: 0; border-top: 1px solid var(--table-line);
  }
  .case-table .head {
    position: absolute; top: 14px; font-family: "Open Sans", sans-serif;
    font-weight: 700; font-size: 18px;
  }
  .head--singular { left: 286px; }
  .head--plural { left: 532px; }
  .case-table .head-line {
    position: absolute; left: 0; right: 0; top: 40px; border-top: 2px solid var(--table-line);
  }
  .case-row {
    position: absolute; left: 0; right: 0; height: 57px;
    border-bottom: 1px solid var(--table-line);
    font-size: 18px; line-height: 1;
  }
  .case-row span { position: absolute; top: 19px; white-space: nowrap; }
  .case-row .case-name { left: 13px; color: var(--case-blue); font-size: 20px; top: 17px; }
  .case-row .singular { left: 275px; }
  .case-row .plural { left: 508px; }
  .row-1 { top: 40px; height: 57px; }
  .row-2 { top: 97px; height: 58px; }
  .row-3 { top: 155px; height: 57px; }
  .row-4 { top: 212px; height: 49px; }
</style>
</head>
<body>

<section class="card card--front">
  <div class="writing-band"></div>

  <div class="ruling ruling--singular">
    <svg width="386" height="82" viewBox="0 0 386 82">
      <g stroke="var(--rule)" stroke-width="1.5">
        <line x1="0" y1="4" x2="386" y2="4"/>
        <line x1="0" y1="27" x2="386" y2="27"/>
        <line x1="0" y1="52" x2="386" y2="52"/>
        <line x1="0" y1="75" x2="386" y2="75"/>
      </g>
      <g fill="none" stroke="var(--house)" stroke-width="2">
        <path d="M2 28 L18 6 L34 28"/>
        <rect x="6" y="27" width="24" height="48"/>
        <line x1="6" y1="52" x2="30" y2="52"/>
        <path d="M10 30 v10 h8 v-10"/>
        <path d="M10 56 h6 v6 h6 v6 h6"/>
      </g>
    </svg>
  </div>
  <div class="ruling ruling--plural">
    <svg width="386" height="82" viewBox="0 0 386 82">
      <g stroke="var(--rule)" stroke-width="1.5">
        <line x1="0" y1="4" x2="386" y2="4"/>
        <line x1="0" y1="27" x2="386" y2="27"/>
        <line x1="0" y1="51" x2="386" y2="51"/>
        <line x1="0" y1="74" x2="386" y2="74"/>
      </g>
      <g fill="none" stroke="var(--house)" stroke-width="2">
        <path d="M2 28 L18 6 L34 28"/>
        <rect x="6" y="27" width="24" height="47"/>
        <line x1="6" y1="51" x2="30" y2="51"/>
        <path d="M10 30 v10 h8 v-10"/>
        <path d="M10 55 h6 v6 h6 v6 h6"/>
      </g>
    </svg>
  </div>

  <p class="word word--singular"><span class="article">der</span> Schwan</p>
  <p class="word word--plural"><span class="article">die</span> Schwäne</p>

  <div class="word-class">
    <svg width="48" height="40" viewBox="0 0 48 40"><polygon points="24,0 48,40 0,40" fill="#000"/></svg>
    <span>Nomen</span>
  </div>

  <div class="picture" role="img" aria-label="Illustration eines blauen Schwans mit ausgebreiteten Flügeln"></div>

  <p class="example-sentence">Der Schwan fliegt über den See.</p>

  <div class="tags">
    <span>Tier</span><span>|</span><span>groß</span><span>|</span><span>weiß</span><span>|</span><span>Vogel</span>
  </div>
</section>

<section class="card card--back">
  <div class="case-band"></div>
  <div class="case-table">
    <div class="top-line"></div>
    <span class="head head--singular">SINGULAR</span>
    <span class="head head--plural">PLURAL</span>
    <div class="head-line"></div>

    <div class="case-row row-1">
      <span class="case-name">Nominativ (wer?/was?)</span>
      <span class="singular">der Schwan</span>
      <span class="plural">die Schwäne</span>
    </div>
    <div class="case-row row-2">
      <span class="case-name">Genitiv (wessen?)</span>
      <span class="singular">des Schwanes, Schwans</span>
      <span class="plural">der Schwäne</span>
    </div>
    <div class="case-row row-3">
      <span class="case-name">Dativ (wem?)</span>
      <span class="singular">dem Schwan</span>
      <span class="plural">den Schwänen</span>
    </div>
    <div class="case-row row-4">
      <span class="case-name">Akkusativ (wen?/was?)</span>
      <span class="singular">den Schwan</span>
      <span class="plural">die Schwäne</span>
    </div>
  </div>
</section>

</body>
</html>
```